New webpage design for development bureau

We are a development bureau in Denmark, and need a design for our webpage. We are called Tindral Development (Part of Tindral Brisk Skolary Group), and are going to aim for multiple markets: Web, Apps, Desktop applications, ect.

We already have a logo, see the uploaded file. We do not have any special demands, other than in have to be simple. A portfolio view should also be available, for future customers.

```html
<!DOCTYPE html>
<html lang="en">
<head>
<meta charset="utf-8">
<title>Tindral Development</title>
<link href="https://fonts.googleapis.com/css2?family=Oswald:wght@300;400;500&family=Open+Sans:ital,wght@0,400;0,600;0,700;1,400&display=swap" rel="stylesheet">
<style>
:root{
  --ink:#1d1f24;
  --navy:#232a35;
  --navy-2:#2c3442;
  --navy-line:#3a4352;
  --orange:#f5a623;
  --muted:#7d838c;
  --soft:#8e96a3;
  --white:#ffffff;
  --rule:#e3e3e3;
}
*{margin:0;padding:0;box-sizing:border-box}
html,body{width:1200px;height:2311px;overflow:hidden;background:var(--white)}
body{position:relative;font-family:"Open Sans",Arial,sans-serif;color:var(--ink)}
.abs{position:absolute}
.display{font-family:"Oswald","Arial Narrow",sans-serif;text-transform:uppercase}

/* header */
.site-header{position:absolute;left:0;top:0;width:1200px;height:78px;background:var(--white)}
.brand{left:111px;top:18px;font-family:"Oswald",sans-serif;font-weight:500;font-size:30px;letter-spacing:1px;color:var(--ink)}
.nav a{position:absolute;top:15px;height:46px;line-height:46px;padding:0 14px;font-family:"Oswald",sans-serif;font-size:16px;color:var(--ink);text-decoration:none;text-transform:uppercase}
.nav a.is-active{background:var(--navy);color:var(--white)}

/* hero */
.hero{position:absolute;left:0;top:78px;width:1200px;height:519px;
  background:linear-gradient(180deg,#3c4a66 0%,#4d5570 40%,#5a4a4a 75%,#3a2e2c 100%)}
.hero-title{width:1200px;text-align:center;color:var(--white)}
.hero-title.big{top:105px;font-size:92px;font-weight:400;line-height:1}
.hero-title.sub{top:200px;font-size:42px;font-weight:400;line-height:56px}
.hero-cta{left:499px;top:344px;width:201px;height:68px;background:var(--orange);color:var(--white);font-family:"Oswald",sans-serif;font-size:18px;text-align:center;line-height:68px;text-transform:uppercase}
.dots{left:578px;top:489px;display:flex;gap:8px}
.dots span{width:7px;height:7px;border-radius:50%;background:rgba(255,255,255,.45)}
.dots span:first-child{background:var(--orange)}

/* intro */
.intro-head{top:632px;width:1200px;text-align:center;font-size:29px;font-weight:400;color:var(--ink)}
.intro-sub{top:680px;width:1200px;text-align:center;font-size:17px;font-weight:300;color:var(--muted)}
.service{top:770px;width:334px;text-align:center}
.service h3{font-family:"Oswald",sans-serif;font-weight:400;font-size:18px;text-transform:uppercase}
.service .icon{width:90px;height:90px;margin:16px auto 18px;border-radius:10px}
.service p{font-size:12px;line-height:20px;padding:0 26px}
.service .more{display:block;margin-top:10px;font-weight:700;font-size:13px}
.divider{top:778px;width:1px;height:200px;background:var(--rule)}

/* who we are */
.about{position:absolute;left:0;top:1071px;width:1200px;height:319px;background:var(--navy)}
.devices{left:128px;top:46px;width:402px;height:194px;border-radius:6px;
  background:linear-gradient(180deg,#4a5160 0%,#2e3440 100%)}
.about h2{left:614px;top:42px;font-family:"Oswald",sans-serif;font-weight:400;font-size:18px;color:var(--white)}
.about .lead{left:614px;top:86px;width:470px;font-size:13px;line-height:21px;color:var(--white)}
.about .body{left:614px;top:148px;width:470px;font-size:11px;line-height:21px;color:var(--soft)}
.about .btn{left:613px;top:231px;width:83px;height:40px;border:1px solid var(--soft);color:var(--soft);font-size:11px;text-align:center;line-height:38px}

/* portfolio */
.portfolio-title{top:1430px;width:1200px;text-align:center;font-size:18px;font-weight:400}
.tabs{left:492px;top:1478px;display:flex;border:1px solid var(--ink)}
.tabs span{height:51px;line-height:51px;padding:0 20px;font-size:12px;border-left:1px solid var(--ink)}
.tabs span:first-child{border-left:0;background:var(--navy);color:var(--white);padding:0 22px}
.shot{top:1555px;width:243px;height:205px}

/* footer */
.footer{position:absolute;left:0;top:1802px;width:1200px;height:509px;background:var(--navy)}
.tweet{left:112px;top:66px;width:250px;height:94px;background:var(--navy-2);border-radius:6px;padding:14px 16px;font-size:11px;line-height:16px;color:var(--soft)}
.tweet em{display:block}
.tweet-tail{left:160px;top:158px}
.avatar{left:417px;top:120px;width:76px;height:76px;border-radius:50%;background:linear-gradient(180deg,#d9d2c8,#a89a8c);border:3px solid #e8e8e8}
.quote{left:530px;top:64px;width:558px;height:122px;background:var(--navy-2);border-radius:6px;padding:16px 18px;font-size:11px;line-height:18px;color:var(--soft)}
.quote cite{display:block;margin-top:14px;color:var(--white);font-size:10px}
.quote-tail{left:516px;top:88px}
.foot-title{top:266px;width:440px;text-align:center;font-family:"Oswald",sans-serif;font-weight:300;font-size:16px;color:var(--soft);text-transform:uppercase}
.foot-box{top:280px;height:101px;border:1px solid var(--navy-line)}
.social{left:128px;top:312px;display:flex;gap:4px}
.social span{width:29px;height:29px;border-radius:50%;background:#4c5563}
.share{left:318px;top:320px;display:flex;gap:6px}
.share span{height:17px;border-radius:2px;background:#5c6677}
.contact-line{font-size:11px;color:var(--soft);display:flex;align-items:center;gap:10px}
.copyright{left:130px;top:420px;font-size:11px;color:var(--soft)}
</style>
</head>
<body>

<header class="site-header">
  <div class="abs brand">TINDRAL</div>
  <nav class="nav">
    <a class="is-active" style="left:645px">Home</a>
    <a style="left:728px">About</a>
    <a style="left:819px">Services</a>
    <a style="left:931px">News</a>
    <a style="left:1018px">Contact</a>
  </nav>
</header>

<section class="hero" role="img" aria-label="Night skyline of city skyscrapers with lit windows">
  <div class="abs display hero-title big">We make</div>
  <div class="abs display hero-title sub">Web,&nbsp; Desktop<br>Apps</div>
  <div class="abs hero-cta">View our services</div>
  <div class="abs dots"><span></span><span></span><span></span></div>
</section>

<h1 class="abs display intro-head">We take an idea, we prototype, we design, we develop, and we release.</h1>
<p class="abs display intro-sub">Attention to detail is our watchword.</p>

<div class="abs service" style="left:99px">
  <h3>Web Applications</h3>
  <div class="icon" role="img" aria-label="Blue globe with magnifying glass" style="background:radial-gradient(circle at 40% 40%,#5fb3f0,#1c6fc0 60%,#fff 61%)"></div>
  <p>Neque porro quisquam est qui dolorem ipsum quia dolor sit amet, consectetur, adipisci velit...</p>
  <span class="more">Read More</span>
</div>
<div class="abs divider" style="left:433px"></div>
<div class="abs service" style="left:432px">
  <h3>Applications</h3>
  <div class="icon" role="img" aria-label="Blue mobile phone" style="width:50px;background:linear-gradient(180deg,#2a8ae0,#0d5cb5)"></div>
  <p>Neque porro quisquam est qui dolorem ipsum quia dolor sit amet, consectetur, adipisci velit...</p>
  <span class="more">Read More</span>
</div>
<div class="abs divider" style="left:766px"></div>
<div class="abs service" style="left:766px">
  <h3>Desktop Applications</h3>
  <div class="icon" role="img" aria-label="Desktop computer monitor" style="background:linear-gradient(180deg,#1d6fd6 0%,#0a3d8a 70%,#d8d8d8 71%,#bfbfbf 100%)"></div>
  <p>Neque porro quisquam est qui dolorem ipsum quia dolor sit amet, consectetur, adipisci velit...</p>
  <span class="more">Read More</span>
</div>

<section class="about">
  <div class="abs devices" role="img" aria-label="Desktop monitor, tablet, laptop and phones grouped together"></div>
  <h2 class="abs display">Who we are</h2>
  <p class="abs lead">Neque porro quisquam est qui dolorem ipsum quia dolor sit amet, consectetur, adipisci velit...</p>
  <p class="abs body">Lorem Ipsum is simply dummy text of the printing and typesetting industry. Lorem Ipsum has been the industry's standard dummy text ever since the 1500s, when an unknown printer took a galley of type and scrambled it to make a type specimen book.</p>
  <div class="abs btn">Learn More</div>
</section>

<h2 class="abs display portfolio-title">Our Portfolio</h2>
<div class="abs tabs"><span>WEB</span><span>APP</span><span>DESKTOP</span></div>
<div class="abs shot" role="img" aria-label="City skyscrapers at dusk" style="left:111px;background:linear-gradient(180deg,#5d6878,#2f3640)">
  <svg width="243" height="205" viewBox="0 0 243 205"><circle cx="121" cy="101" r="8" fill="none" stroke="#fff" stroke-width="2"/><line x1="127" y1="107" x2="133" y2="113" stroke="#fff" stroke-width="3"/><line x1="117" y1="101" x2="125" y2="101" stroke="#fff" stroke-width="2"/><line x1="121" y1="97" x2="121" y2="105" stroke="#fff" stroke-width="2"/></svg>
</div>
<div class="abs shot" role="img" aria-label="Illuminated iron tower at night" style="left:355px;background:linear-gradient(180deg,#2c2f3a,#3a3530 60%,#6a4a20)"></div>
<div class="abs shot" role="img" aria-label="Gothic clock tower" style="left:599px;background:linear-gradient(90deg,#d5d8d6,#555a55 50%,#c9ccca)"></div>
<div class="abs shot" role="img" aria-label="Red brick towers under blue sky" style="left:843px;background:linear-gradient(180deg,#9fc0e6,#c97a5e 60%,#8a5a48)"></div>

<footer class="footer">
  <div class="abs tweet">The app we've been working on for quite a while is now submitted #tindralbuild tindral.dk/a/7Rk2<em>2 days ago</em></div>
  <svg class="abs tweet-tail" width="40" height="30"><path d="M0 0 L40 0 L0 28 Z" fill="#2c3442"/></svg>
  <div class="abs avatar" role="img" aria-label="Portrait of the founder"></div>
  <svg class="abs quote-tail" width="16" height="24"><path d="M16 0 L0 12 L16 24 Z" fill="#2c3442"/></svg>
  <div class="abs quote">Lorem Ipsum is simply dummy text of the printing and typesetting industry. Lorem Ipsum has been the industry's standard dummy text ever since the 1500s,<cite>-Founder of Tindral-</cite></div>

  <div class="abs foot-title" style="left:112px">Get connect with us</div>
  <div class="abs foot-box" style="left:112px;width:439px"></div>
  <div class="abs social"><span></span><span></span><span></span><span></span></div>
  <div class="abs share"><span style="width:38px"></span><span style="width:22px"></span><span style="width:48px"></span><span style="width:22px"></span><span style="width:28px"></span><span style="width:22px"></span></div>

  <div class="abs foot-title" style="left:653px">Contact with us</div>
  <div class="abs foot-box" style="left:653px;width:435px"></div>
  <div class="abs contact-line" style="left:676px;top:298px">
    <svg width="10" height="13" viewBox="0 0 10 13"><path d="M5 0a5 5 0 0 1 5 5c0 3-5 8-5 8S0 8 0 5a5 5 0 0 1 5-5z" fill="#8e96a3"/><circle cx="5" cy="5" r="2" fill="#232a35"/></svg>
    Lorem Ipsum is simply dummy text of the printing
  </div>
  <div class="abs contact-line" style="left:676px;top:338px">
    <svg width="12" height="12" viewBox="0 0 12 12"><path d="M2 0l3 3-1.5 1.5a7 7 0 0 0 4 4L9 7l3 3-2 2C5 12 0 7 0 2z" fill="#8e96a3"/></svg>
    +45 31 40 72 58
  </div>
  <div class="abs contact-line" style="left:858px;top:338px">
    <svg width="14" height="10" viewBox="0 0 14 10"><rect width="14" height="10" fill="#8e96a3"/><path d="M0 0l7 5 7-5" fill="none" stroke="#232a35"/></svg>
    hello@tindral-dev.dk
  </div>

  <div class="abs copyright">Copyright © 2014</div>
</footer>

</body>
</html>
```